Professional business podcast cover

Hey guys,

I want to redesign my podcast cover from the Vimpa Podcast.

It is a professional business podcast for small and medium sized business. Therefor I need something professional.
No fancy glitter designs.
Something real clean and easy.

I am thinking about something similar to this pic.
https://snapvault.example/7Qk2Lm9xP4aZ

What is important for the design?

1. professional and clean look
2. fonts= roboto
3. the logo must be readable also on small devices (please do not change the existing logo!)
4. same color as the logo
5. my full name must be included in the design: Joss Belder

Thank you for your work.

I can not wait to get your designs.

Regards

Joss from Vimpa

Reason: I need a perfect fitting timeless design. If it needs more time to be generated, than we do so.

Target Market(s)

Small and medium sized CEOs

Industry/Entity Type

Consulting

Font styles to use
Sans Serif

Colors
acd136

Requirements
Must have
• 1. professional and clean look
• 2. fonts= roboto
• 3. the logo must be readable also on small devices
• 4. same color as the logo
• 5. size 1400x 1400
• 6. Text: Joss Belder very present
Nice to have
• Get inspired by covers like Dale Korvin, Gus Pellmore or Neil Ostrands podcast.
• https://snapvault.example/4Rb8Tn2wQ6cY
• https://snapvault.example/9Hd3Vj5sK1eX
• https://snapvault.example/2Mf6Pw8uL3gW
Should not have
• Fancy glossi shinny designs

```html
<!DOCTYPE html>
<html lang="de">
<head>
<meta charset="utf-8">
<title>Vimpa Podcast Cover</title>
<link rel="stylesheet" href="https://fonts.googleapis.com/css2?family=Roboto:wght@400;700&display=swap">
<style>
  :root {
    --page-white: #ffffff;
    --panel-sage: #c5d1bf;
    --brand-green: #39b54a;
    --band-green: #1d6d3c;
    --text-white: #ffffff;
    --host-hair: #c07a4c;
    --host-skin: #dcaa92;
    --host-suit: #222a3e;
    --host-suit-deep: #171c2b;
  }
  html, body {
    margin: 0;
    padding: 0;
    width: 1200px;
    height: 1200px;
    overflow: hidden;
    background: var(--page-white);
  }
  .cover {
    position: relative;
    width: 1200px;
    height: 1200px;
    background: var(--page-white);
    font-family: "Roboto", Arial, sans-serif;
  }
  .cover-panel {
    position: absolute;
    left: 38px;
    top: 38px;
    width: 1124px;
    height: 1124px;
    background: var(--panel-sage);
    overflow: hidden;
  }
  .host-portrait {
    position: absolute;
    left: 0;
    top: 0;
    width: 1124px;
    height: 1124px;
  }
  .host-name {
    position: absolute;
    left: 46px;
    top: 90px;
    margin: 0;
    font-size: 70px;
    font-weight: 700;
    line-height: 1;
    color: var(--band-green);
    letter-spacing: 1px;
    text-transform: uppercase;
  }
  .brand-mark {
    position: absolute;
    left: 44px;
    top: 500px;
    display: flex;
    align-items: center;
    gap: 20px;
  }
  .brand-dot {
    width: 70px;
    height: 70px;
    border-radius: 50%;
    background: var(--brand-green);
  }
  .brand-name {
    font-size: 160px;
    font-weight: 400;
    line-height: 1;
    color: var(--brand-green);
  }
  .tagline-band {
    position: absolute;
    left: 0;
    top: 710px;
    width: 1124px;
    height: 185px;
    background: var(--band-green);
    opacity: 0.95;
    box-sizing: border-box;
    padding: 20px 0 0 46px;
  }
  .tagline {
    margin: 0;
    font-size: 72px;
    font-weight: 700;
    line-height: 86px;
    color: var(--text-white);
    letter-spacing: 1px;
    text-transform: uppercase;
  }
</style>
</head>
<body>
  <div class="cover">
    <div class="cover-panel">
      <svg class="host-portrait" viewBox="0 0 1124 1124" role="img" aria-label="Portrait photo of host Joss Belder in dark suit, white shirt and green tie">
        <defs>
          <linearGradient id="hostTone" x1="0" y1="20" x2="0" y2="1124" gradientUnits="userSpaceOnUse">
            <stop offset="0" stop-color="var(--host-hair)"/>
            <stop offset="0.5" stop-color="var(--host-skin)"/>
            <stop offset="0.62" stop-color="var(--host-suit)"/>
            <stop offset="1" stop-color="var(--host-suit-deep)"/>
          </linearGradient>
        </defs>
        <path fill="url(#hostTone)" d="M650 300 C640 120 760 18 870 18 C990 18 1060 120 1050 300 L1030 520 C1015 600 1000 640 1030 665 L1124 710 L1124 1124 L230 1124 L290 820 C320 730 600 690 690 655 C675 600 660 520 650 300 Z"/>
      </svg>
      <p class="host-name">Joss Belder</p>
      <div class="brand-mark">
        <span class="brand-dot"></span>
        <span class="brand-name">Vimpa</span>
      </div>
      <div class="tagline-band">
        <h1 class="tagline">Unternehmerwissen<br>umsetzbar in 15 Minuten</h1>
      </div>
    </div>
  </div>
</body>
</html>
```